Web Design Project

I am looking for a simple website to promote my business called Wyllard Benick Consulting. We provide consulting and implementation services for finance and supply chain processes and systems.

We want to project a professional but innovative image. I have attached a copy of our logo. It is not necessary to stick with the colours in the logo - we encourage you to experiment with the colours and even to change the colours of the logo to fit with your design. Although, on the front page we would like to have the logo with its original colours.

Required sections:
About
What we do
Clients
Contact
Updates

Target Market(s)

Medium to large companies including multi-nationals in all industries.

Industry/Entity Type

Finance

Requirements
Must have
• Required sections:
About
What we do
Clients
Contact

```html
<!DOCTYPE html>
<html lang="en">
<head>
<meta charset="utf-8">
<title>Wyllard Benick Consulting</title>
<link rel="stylesheet" href="https://fonts.googleapis.com/css2?family=Arimo:wght@400;700&display=swap">
<style>
:root{
  --blue:#0a5bab;
  --green:#97b20f;
  --lime:#bdd43c;
  --ink:#1b1b1b;
  --body:#7a7a7a;
  --panel:#f2f2f2;
  --strip:#e4e4e4;
  --rule:#d6d6d6;
  --footer:#2a2a2a;
  --footer-text:#bdbdbd;
}
*{box-sizing:border-box;margin:0;padding:0}
html,body{width:1200px;height:1192px;overflow:hidden}
body{position:relative;font-family:"Arimo",Arial,sans-serif;background:var(--panel);color:var(--ink)}
.abs{position:absolute}

/* header */
.site-header{left:0;top:0;width:1200px;height:136px;background:#fff;border-bottom:4px solid var(--lime)}
.brand{left:157px;top:30px;display:flex;align-items:center;gap:10px;color:var(--blue);font-weight:700}
.brand-mark{width:40px;height:40px;border-radius:50%;background:var(--blue);flex:none}
.brand-name{font-size:16px;line-height:20px;letter-spacing:.5px;white-space:nowrap}
.phone{left:889px;top:30px;display:flex;align-items:center;gap:6px;color:var(--blue);font-weight:700;font-size:17px;white-space:nowrap}
.main-nav{left:525px;top:63px;width:520px;height:38px}
.main-nav a{font-size:14.5px;font-weight:700;color:var(--ink);text-decoration:none;letter-spacing:.3px;white-space:nowrap}
.nav-item{position:absolute;top:0;height:38px;line-height:38px;white-space:nowrap}
.nav-active{left:0;width:84px;background:var(--blue);border-radius:3px;text-align:center}
.nav-active a{color:#fff}
.nav-sep{position:absolute;top:8px;width:1px;height:24px;background:var(--rule)}

/* hero */
.hero{left:0;top:136px;width:1200px;height:418px;background:linear-gradient(100deg,#e9ecef 0%,#c9ced4 35%,#d7dbe0 55%,#9ea7b1 85%,#7f8a96 100%)}
.headline{left:157px;top:277px;width:494px;height:54px;background:var(--green);color:#fff;font-weight:700;font-size:29px;line-height:54px;padding-left:16px;white-space:nowrap}
.subline{left:157px;top:340px;width:329px;height:41px;background:var(--blue);color:#fff;font-weight:700;font-size:22px;line-height:42px;padding-left:18px;white-space:nowrap}
.slider-dot{top:509px;width:22px;height:22px;border-radius:50%;background:#fff;padding:4px}
.slider-dot span{display:block;width:14px;height:14px;border-radius:50%;background:var(--blue)}

/* services */
.service{top:579px;width:280px;text-align:center}
.service-icon{width:60px;height:60px;margin:0 auto;display:block}
.service h2{margin-top:16px;font-size:17px;font-weight:700;letter-spacing:.3px;white-space:nowrap}
.service p{margin-top:13px;font-size:13px;line-height:18.5px;color:var(--body)}
.btn{display:inline-block;background:var(--green);color:#fff;font-size:14px;text-decoration:none;height:33px;line-height:33px;padding:0 18px;border-radius:2px;white-space:nowrap}
.service .btn{margin-top:12px;width:103px;padding:0}
.divider{left:157px;top:808px;width:886px;height:1px;background:var(--rule)}

/* who we are */
.section-title{top:838px;font-size:16.5px;font-weight:700;letter-spacing:.3px;white-space:nowrap}
.about-text{left:157px;top:868px;width:584px;font-size:13px;line-height:16.6px;color:var(--body)}
.arrow{top:933px;width:23px;height:23px;background:var(--green)}
.clients{left:157px;top:962px;width:581px;height:101px;background:var(--strip)}
.client{position:absolute;top:0;height:101px;display:flex;align-items:center;justify-content:center;font-size:18px;font-weight:700;color:#5a5a5a;white-space:nowrap}
.client-sep{position:absolute;top:18px;width:1px;height:66px;background:#cfcfcf}
.feature-img{left:766px;top:869px;width:277px;height:124px;background:linear-gradient(100deg,#dfe3e7,#b8c0c8 50%,#8b96a2)}
.feature-btn{left:941px;top:959px;width:102px;height:34px;line-height:34px;text-align:center;padding:0;border-radius:0}
.feature-text{left:766px;top:1000px;width:280px;font-size:13px;line-height:16.6px;color:var(--body)}

/* footer */
.site-footer{left:0;top:1099px;width:1200px;height:93px;background:var(--footer)}
.footer-nav{left:155px;top:1118px;font-size:12px;color:var(--footer-text);display:flex;gap:14px;white-space:nowrap}
.footer-nav a{color:var(--footer-text);text-decoration:none}
.copyright{right:156px;top:1118px;font-size:12px;color:var(--footer-text);white-space:nowrap}
</style>
</head>
<body>

<header class="site-header abs">
  <div class="brand abs">
    <span class="brand-mark"></span>
    <span class="brand-name">WYLLARD BENICK<br>CONSULTING LIMITED</span>
  </div>
  <div class="phone abs">
    <svg width="28" height="20" viewBox="0 0 28 20"><path d="M2 7C2 2 26 2 26 7v2h-6V6H8v3H2z" fill="#0a5bab"/><path d="M7 9h14l3 10H4z" fill="#0a5bab"/><circle cx="14" cy="14" r="3" fill="#fff"/></svg>
    <span>: 5550-318-272</span>
  </div>
  <nav class="main-nav abs">
    <div class="nav-item nav-active"><a href="#">HOME</a></div>
    <div class="nav-item" style="left:108px"><a href="#">ABOUT</a></div>
    <span class="nav-sep" style="left:178px"></span>
    <div class="nav-item" style="left:203px"><a href="#">WHAT WE DO</a></div>
    <span class="nav-sep" style="left:315px"></span>
    <div class="nav-item" style="left:339px"><a href="#">CLIENTS</a></div>
    <span class="nav-sep" style="left:422px"></span>
    <div class="nav-item" style="left:444px"><a href="#">CONTACT</a></div>
  </nav>
</header>

<section class="hero abs" role="img" aria-label="Photo of a business team smiling around a meeting table while two colleagues shake hands"></section>
<div class="headline abs">BUILDING YOUR BUSINESS WITH</div>
<div class="subline abs">GROWTH &amp; PROSPERITY</div>
<div class="slider-dot abs" style="left:552px"><span></span></div>
<div class="slider-dot abs" style="left:587px"><span></span></div>
<div class="slider-dot abs" style="left:618px"><span></span></div>

<section class="service abs" style="left:155px">
  <svg class="service-icon" viewBox="0 0 60 60"><circle cx="30" cy="30" r="30" fill="#0a5bab"/><circle cx="30" cy="30" r="17" fill="none" stroke="#fff" stroke-width="4"/><text x="30" y="38" text-anchor="middle" font-family="Arimo,Arial,sans-serif" font-weight="700" font-size="22" fill="#fff">$</text></svg>
  <h2>FINANACIAL CONSULTING</h2>
  <p>Lorem Ipsum is simply dummy text of the printing and typesetting industry. Lorem Ipsum has been the industry's standard dummy</p>
  <a class="btn" href="#">Read More</a>
</section>
<section class="service abs" style="left:460px">
  <svg class="service-icon" viewBox="0 0 60 60"><circle cx="30" cy="30" r="30" fill="#0a5bab"/><circle cx="27" cy="20" r="7" fill="#fff"/><path d="M16 38c0-8 5-11 11-11s11 3 11 11z" fill="#fff"/><rect x="20" y="38" width="24" height="8" fill="#fff"/></svg>
  <h2>MARKET ASSESSMENT</h2>
  <p>Lorem Ipsum is simply dummy text of the printing and typesetting industry. Lorem Ipsum has been the industry's standard dummy</p>
  <a class="btn" href="#">Read More</a>
</section>
<section class="service abs" style="left:765px">
  <svg class="service-icon" viewBox="0 0 60 60"><circle cx="30" cy="30" r="30" fill="#0a5bab"/><ellipse cx="30" cy="23" rx="8" ry="10" fill="#fff"/><path d="M15 47c0-10 7-13 15-13s15 3 15 13z" fill="#fff"/></svg>
  <h2>REGULATORY SUPPORT</h2>
  <p>Lorem Ipsum is simply dummy text of the printing and typesetting industry. Lorem Ipsum has been the industry's standard dummy</p>
  <a class="btn" href="#">Read More</a>
</section>

<div class="divider abs"></div>

<h2 class="section-title abs" style="left:157px">WHO WE ARE</h2>
<p class="about-text abs">Lorem Ipsum is simply dummy text of the printing and typesetting industry. Lorem Ipsum has been the industry's standard dummy text ever since the 1500s, when an unknown printer took a galley of type and scrambled it to make a type specimen book. It has survived not only five centuries, but also the leap into electronic typesetting, remaining essentially unchanged. It was</p>
<a class="arrow abs" href="#" style="left:686px" aria-label="Previous"><svg width="23" height="23" viewBox="0 0 23 23"><path d="M14 6l-6 5.5 6 5.5" fill="none" stroke="#fff" stroke-width="2.5"/></svg></a>
<a class="arrow abs" href="#" style="left:714px" aria-label="Next"><svg width="23" height="23" viewBox="0 0 23 23"><path d="M9 6l6 5.5-6 5.5" fill="none" stroke="#fff" stroke-width="2.5"/></svg></a>

<div class="clients abs">
  <div class="client" style="left:0;width:146px">Halvern Studio</div>
  <span class="client-sep" style="left:146px"></span>
  <div class="client" style="left:147px;width:138px">Tamrik</div>
  <span class="client-sep" style="left:285px"></span>
  <div class="client" style="left:286px;width:148px">Ostrava</div>
  <span class="client-sep" style="left:434px"></span>
  <div class="client" style="left:435px;width:146px">Tamrik</div>
</div>

<h2 class="section-title abs" style="left:767px">WHO WE ARE</h2>
<div class="feature-img abs" role="img" aria-label="Photo of the consulting team at a meeting table with a handshake"></div>
<a class="btn feature-btn abs" href="#">Read More</a>
<p class="feature-text abs">Lorem Ipsum is simply dummy text of the printing and typesetting industry. Lorem Ipsum has been the industry's standard dummy text ever since the 1500s, when an unknown printer</p>

<footer class="site-footer abs"></footer>
<nav class="footer-nav abs">
  <a href="#">Home</a><span>|</span><a href="#">About</a><span>|</span><a href="#">What we do</a><span>|</span><a href="#">Clients</a><span>|</span><a href="#">Contact</a>
</nav>
<p class="copyright abs">Wyllard Benick © 2013. All rights Reserved</p>

</body>
</html>
```